Large Christian Church organization website design

This website design is an advanced design ultimately requiring design for at least 4 pages, but starting with only one.

I am looking for an "award winning" design. I have made this easy as I have the functionality and general flow prototyped in an HTML prototype. I recorded videos to explain these in depth and will attach the HTML prototype as well.

The design must focused on connecting with people who need physical, emotional or spiritual help. It will be a website designed to meet people where they are and to help bring them along in there relationship to God.

Please work on this design only if you have a heart for people connecting with Christians and God.

A couple designers have asked me about the brief... did you have trouble downloading the brief for this project from this page:

If so, perhaps you can email me directly and I can send to you... you can email me: dmitri@pewlantern.org.
Also, would love to know if you still plan on creating a design for this project, thanks!

Reason: Still looking for a design that matches the functionality we need and provides a fantastic home run look and feel that is warm, inviting and friendly...

Reason: Need more time to provide feedback, request edits...

Target Market(s)

See creative brief

Industry/Entity Type

Church

Requirements
Must have
• The latest creative brief can be found here:

https://files.velmora.net/a/quostrel.com/sheet/d/7H3kPzW2mQ9rTx4LbN8vYcJ5dFa0GsE1uRoKi6wq/view?hl=en_US#mark=id.tqzlowhrva7k

```html
<!DOCTYPE html>
<html lang="en">
<head>
<meta charset="utf-8">
<title>Red River Conference</title>
<link href="https://fonts.googleapis.com/css2?family=Open+Sans:wght@400;600&family=Crimson+Text&display=swap" rel="stylesheet">
<style>
:root{
  --orange-top:#d9801f;
  --orange-mid:#e8932e;
  --orange-light:#f3b05a;
  --footer:#c9782c;
  --dark:#1c1c1c;
  --dark-2:#333;
  --red:#c9140f;
  --white:#fff;
  --green:#4a8a16;
  --nav-orange:#f08a1c;
  --muted:#7d7d7d;
}
*{margin:0;padding:0;box-sizing:border-box}
html,body{width:1200px;height:1124px;overflow:hidden;background:var(--footer)}
body{font-family:"Open Sans",Arial,sans-serif}
.page{width:1000px;height:937px;transform:scale(1.2);transform-origin:0 0;position:relative;overflow:hidden}

.site-header{position:absolute;left:0;top:0;width:1000px;height:167px;
  background:linear-gradient(#3a3a3a,#111 100%)}
.topbar{position:absolute;left:0;top:0;width:1000px;height:55px;
  background:linear-gradient(#c96f12,var(--orange-top))}
.logo-tab{position:absolute;left:12px;top:30px;width:363px;height:137px;
  background:linear-gradient(#3a3a3a,#1a1a1a);border-radius:12px 12px 0 0}
.brand{position:absolute;left:36px;top:50px;display:flex;align-items:center;gap:12px}
.brand-mark{width:40px;height:40px;background:var(--red);border-radius:50%}
.brand-name{color:var(--white);font-weight:600;font-size:17px;line-height:1.15;width:290px}
.tagline{position:absolute;left:88px;top:96px;color:#e0261a;font-size:14px;font-weight:400}

.utility{position:absolute;top:17px;left:646px;display:flex;align-items:center;gap:9px}
.utility svg{display:block}
.social-dot{width:22px;height:22px;border-radius:50%}
.search{position:absolute;left:831px;top:19px;width:151px;height:21px;background:var(--white);border:1px solid #ccc}
.search svg{position:absolute;right:5px;top:3px}

.main-nav{position:absolute;top:55px;left:555px;display:flex}
.main-nav a{display:block;height:29px;line-height:29px;padding:0 18px;color:var(--nav-orange);text-decoration:none;font-size:13px}
.main-nav a.active{background:linear-gradient(#e0851f,#c86a10);color:var(--white);border-radius:0 0 5px 5px}
.sub-nav{position:absolute;top:130px;left:400px;display:flex;gap:28px;align-items:center}
.sub-nav a{color:var(--white);text-decoration:none;font-size:15px}
.sub-nav a.active{background:linear-gradient(#e2261e,#a30d08);padding:3px 21px;border-radius:5px;position:relative}
.sub-nav a.active::after{content:"";position:absolute;left:50%;bottom:-6px;margin-left:-6px;
  border:6px solid transparent;border-bottom:0;border-top-color:#a30d08}

.hero{position:absolute;left:0;top:167px;width:1000px;height:331px;
  background:linear-gradient(90deg,#d57a1b,var(--orange-mid) 50%,#d57a1b)}
.slide{position:absolute;left:65px;top:13px;width:867px;height:313px;border:3px solid var(--white);border-radius:18px;overflow:hidden;
  background:linear-gradient(90deg,#6a4a38,#b58a70 30%,#d4a285 50%,#a07058 70%,#7a4030);box-shadow:0 4px 10px rgba(0,0,0,.3)}
.slide-caption{position:absolute;left:0;bottom:0;width:100%;height:47px;background:rgba(10,10,10,.88);color:var(--white);
  text-align:center;font-size:25px;line-height:47px}
.arrow{position:absolute;width:23px;height:21px;border-radius:4px;background:#f0d2a8;display:flex;align-items:center;justify-content:center}
.arrow.prev{left:28px;top:139px}
.arrow.next{left:947px;top:150px}

.quick-links{position:absolute;left:0;top:498px;width:1000px;height:149px;
  background:radial-gradient(ellipse at 50% 60%,#fff3dc 0%,var(--orange-light) 40%,#de8425 100%)}
.thumb{position:absolute;top:21px;width:129px;height:101px;background:var(--white);padding:4px;box-shadow:0 1px 3px rgba(0,0,0,.2)}
.thumb-img{width:121px;height:75px}
.thumb-label{font-family:"Crimson Text",Georgia,serif;font-size:11px;color:var(--green);text-align:center;margin-top:4px;white-space:nowrap}

.site-footer{position:absolute;left:0;top:647px;width:1000px;height:250px;background:var(--footer)}
.footer-brand{position:absolute;left:112px;top:95px;display:flex;align-items:center;gap:8px;color:var(--white);font-weight:600;font-size:13px;width:110px;line-height:1.2}
.footer-brand span.dot{flex:0 0 auto;width:18px;height:18px;border-radius:50%;background:#e24a1e}
.link-col{position:absolute;top:28px;color:var(--white)}
.link-col h3{font-weight:400;font-size:16px;margin-bottom:28px}
.link-col a{display:block;color:var(--white);text-decoration:none;font-size:12.5px;line-height:24px}
.bottom-bar{position:absolute;left:0;top:897px;width:1000px;height:40px;background:linear-gradient(#2a2a2a,#111)}
.copyright{position:absolute;left:0;width:1000px;top:13px;text-align:center;font-size:9.5px;color:var(--muted);padding-right:28px}
.bottom-social{position:absolute;left:865px;top:9px;display:flex;gap:12px}
</style>
</head>
<body>
<div class="page">
  <header class="site-header">
    <div class="topbar"></div>
    <div class="logo-tab"></div>
    <div class="brand">
      <span class="brand-mark"></span>
      <span class="brand-name">RED RIVER CONFERENCE of The Wesleyan Fellowship Church</span>
    </div>
    <div class="tagline">Reaching out to the Heart of Red River</div>

    <div class="utility">
      <svg width="24" height="24" viewBox="0 0 24 24"><polygon points="12,1 15,9 23,9 16.5,14 19,22 12,17 5,22 7.5,14 1,9 9,9" fill="#f6c21b" stroke="#b67d0a"/></svg>
      <svg width="24" height="24" viewBox="0 0 24 24"><polygon points="12,3 22,12 19,12 19,21 5,21 5,12 2,12" fill="#fff" stroke="#2a6fb8" stroke-width="1.5"/><rect x="10" y="14" width="4" height="7" fill="#2a6fb8"/></svg>
      <svg width="16" height="24" viewBox="0 0 16 24"><text x="8" y="20" text-anchor="middle" font-family="Open Sans,sans-serif" font-size="22" font-weight="600" fill="#f3e2c6">?</text></svg>
      <span class="social-dot" style="background:#f38b1b;border:2px solid #fff3"></span>
      <span class="social-dot" style="background:#3fa4e0"></span>
      <span class="social-dot" style="background:#2f6fc7"></span>
    </div>
    <div class="search">
      <svg width="14" height="14" viewBox="0 0 14 14"><circle cx="5.5" cy="5.5" r="4" fill="none" stroke="#2a8ad8" stroke-width="2"/><line x1="8.5" y1="8.5" x2="13" y2="13" stroke="#2a8ad8" stroke-width="2.5"/></svg>
    </div>

    <nav class="main-nav">
      <a class="active" href="#">RWF News</a>
      <a href="#">RRC News</a>
      <a href="#">Events</a>
      <a href="#">Employment</a>
    </nav>
    <nav class="sub-nav">
      <a class="active" href="#">Welcome Menu</a>
      <a href="#">Church Menu</a>
    </nav>
  </header>

  <section class="hero">
    <div class="slide" role="img" aria-label="Photo of a smiling young boy in a knit cap">
      <div class="slide-caption">I Need Help....</div>
    </div>
    <span class="arrow prev"><svg width="8" height="10" viewBox="0 0 8 10"><polygon points="7,0 7,10 0,5" fill="#222"/></svg></span>
    <span class="arrow next"><svg width="8" height="10" viewBox="0 0 8 10"><polygon points="1,0 1,10 8,5" fill="#222"/></svg></span>
  </section>

  <section class="quick-links">
    <div class="thumb" style="left:79px"><div class="thumb-img" role="img" aria-label="Smiling boy" style="background:linear-gradient(#2c3448,#c99a7a 60%,#e7c0a0)"></div><div class="thumb-label">I Need Help...</div></div>
    <div class="thumb" style="left:222px"><div class="thumb-img" role="img" aria-label="Woman praying" style="background:linear-gradient(120deg,#3a2a22,#a27860 60%,#d9b8a0)"></div><div class="thumb-label">I Need God...</div></div>
    <div class="thumb" style="left:365px"><div class="thumb-img" role="img" aria-label="Hands folded over a Bible" style="background:linear-gradient(#141414,#6a4a2a 60%,#b08050)"></div><div class="thumb-label">I Need a Church....</div></div>
    <div class="thumb" style="left:508px"><div class="thumb-img" role="img" aria-label="Family unpacking moving boxes" style="background:linear-gradient(#f1e8d8,#d7b890 60%,#b98a5a)"></div><div class="thumb-label">Moving to North Texas ?</div></div>
    <div class="thumb" style="left:651px"><div class="thumb-img" role="img" aria-label="White church building under blue sky" style="background:linear-gradient(#5a8ad4,#9fc0ea 50%,#e8eef4)"></div><div class="thumb-label">What is Wesleyan Fellowship ?</div></div>
    <div class="thumb" style="left:794px"><div class="thumb-img" role="img" aria-label="Volunteers repairing a house" style="background:linear-gradient(#9ab8d8,#c6c0b4 50%,#b03a2a)"></div><div class="thumb-label">I Want to Serve</div></div>
  </section>

  <footer class="site-footer">
    <div class="footer-brand"><span class="dot"></span>Red River Conference</div>
    <div class="link-col" style="left:269px"><h3>Category</h3><a href="#">Commonly Used Link</a><a href="#">Commonly Used Link</a><a href="#">Commonly Used Link</a><a href="#">Commonly Used Link</a><a href="#">Commonly Used Link</a><a href="#">Commonly Used Link</a></div>
    <div class="link-col" style="left:414px;top:29px"><h3>Category</h3><a href="#">Commonly Used Link</a><a href="#">Commonly Used Link</a><a href="#">Commonly Used Link</a><a href="#">Commonly Used Link</a><a href="#">Commonly Used Link</a><a href="#">Commonly Used Link</a></div>
    <div class="link-col" style="left:559px;top:29px"><h3>Category</h3><a href="#">Commonly Used Link</a><a href="#">Commonly Used Link</a><a href="#">Commonly Used Link</a><a href="#">Commonly Used Link</a><a href="#">Commonly Used Link</a><a href="#">Commonly Used Link</a></div>
    <div class="link-col" style="left:706px;top:25px"><h3>Category</h3><a href="#">Commonly Used Link</a><a href="#">Commonly Used Link</a><a href="#">Commonly Used Link</a><a href="#">Commonly Used Link</a><a href="#">Commonly Used Link</a><a href="#">Commonly Used Link</a></div>
  </footer>

  <div class="bottom-bar">
    <div class="copyright">Copyright (c) 2011. www.redriverconference.org</div>
    <div class="bottom-social">
      <span class="social-dot" style="background:#f38b1b"></span>
      <span class="social-dot" style="background:#3fa4e0"></span>
      <span class="social-dot" style="background:#2f6fc7"></span>
    </div>
  </div>
</div>
</body>
</html>
```